Financial Planning firm focused on serving women 55-65 yrs old needs stationary design

We are rebranding our financial planning firm and our target client is a 55-65 yr old women. We need a stationary design to go with our new logo.

Contact Information: Raymond Kessler, MS, CFP President Harlow Wealth Management 4820 Bramblewood Lane, Suite 317 Estero, FL 33961 ray@harlowwealthmgmt.example phone 239-555-0184

```html
<!DOCTYPE html>
<html lang="en">
<head>
<meta charset="utf-8">
<title>Harlow Wealth Management – Business Card</title>
<link href="https://fonts.googleapis.com/css2?family=Open+Sans:wght@400;600;700&display=swap" rel="stylesheet">
<style>
  :root {
    --backdrop: #5b4535;
    --card-white: #fbfbf8;
    --brand-blue: #2f5f8f;
    --sage: #9fb5a0;
    --band-navy: #3d4a80;
    --ink: #333333;
    --divider: #5a3a7a;
    --reverse-blue: #2e6a96;
    --rule: #8aa0b8;
  }
  * { margin: 0; padding: 0; box-sizing: border-box; }
  html, body { width: 1200px; height: 771px; overflow: hidden; }
  body {
    background: var(--backdrop);
    font-family: "Open Sans", sans-serif;
    position: relative;
  }
  .card {
    position: absolute;
    width: 600px;
    height: 342px;
  }
  .card-front { left: 120px; top: 21px; background: var(--card-white); }
  .card-back { left: 477px; top: 393px; background: var(--reverse-blue); }

  .brand {
    position: absolute;
    left: 0; top: 0; width: 100%; height: 213px;
  }
  .brand-circle {
    position: absolute;
    left: 139px; top: 43px;
    width: 104px; height: 104px;
    border-radius: 50%;
    background: var(--sage);
  }
  .brand-rule {
    position: absolute;
    left: 262px; width: 200px; height: 1px;
    background: var(--rule);
  }
  .brand-rule.top { top: 58px; }
  .brand-rule.bottom { top: 140px; }
  .brand-name {
    position: absolute;
    left: 262px; top: 62px; width: 200px;
    color: var(--brand-blue);
    font-weight: 600;
    text-transform: uppercase;
    line-height: 1;
  }
  .brand-name .word-main { display: block; font-size: 54px; letter-spacing: 1px; }
  .brand-name .word-sub { display: block; font-size: 13px; letter-spacing: 0.6px; margin-top: 6px; }

  .name-band {
    position: absolute;
    left: 0; top: 192px; width: 100%; height: 36px;
    background: var(--band-navy);
    color: #ffffff;
    text-align: center;
    line-height: 36px;
  }
  .name-band .person { font-weight: 700; font-size: 18px; }
  .name-band .title { font-size: 13px; margin-left: 4px; }

  .contact {
    position: absolute;
    left: 30px; top: 262px;
    font-size: 14px; color: var(--ink);
    line-height: 24px;
  }
  .contact-line { display: flex; align-items: center; gap: 10px; }
  .contact-line svg { width: 13px; height: 13px; flex: none; }

  .divider {
    position: absolute;
    left: 319px; top: 256px;
    width: 2px; height: 60px;
    background: var(--divider);
  }
  .address {
    position: absolute;
    right: 30px; top: 262px;
    text-align: right;
    font-size: 14px; color: var(--ink);
    line-height: 24px;
  }

  .back-circle {
    position: absolute;
    left: 210px; top: 81px;
    width: 180px; height: 180px;
    border-radius: 50%;
    background: #ffffff;
  }
</style>
</head>
<body>
  <section class="card card-front">
    <div class="brand">
      <div class="brand-circle"></div>
      <div class="brand-rule top"></div>
      <div class="brand-name">
        <span class="word-main">Harlow</span>
        <span class="word-sub">Wealth Management</span>
      </div>
      <div class="brand-rule bottom"></div>
    </div>

    <div class="name-band">
      <span class="person">Raymond Kessler</span><span class="title">MS, CFP President</span>
    </div>

    <div class="contact">
      <div class="contact-line">
        <svg viewBox="0 0 16 16" aria-hidden="true"><path d="M3.5 1.5l2.5 0.5 1 3-1.6 1.3a9 9 0 0 0 4.3 4.3L11 9l3 1 0.5 2.5c-0.3 1-1.3 1.8-2.5 1.8C6 14.3 1.7 10 1.7 4c0-1.2 0.8-2.2 1.8-2.5z" fill="none" stroke="#333" stroke-width="1.4"/></svg>
        <span>239-555-0184</span>
      </div>
      <div class="contact-line">
        <svg viewBox="0 0 16 16" aria-hidden="true"><rect x="1.5" y="3.5" width="13" height="9" fill="none" stroke="#333" stroke-width="1.4"/><path d="M1.5 3.5L8 9l6.5-5.5" fill="none" stroke="#333" stroke-width="1.4"/></svg>
        <span>ray@harlowwealthmgmt.example</span>
      </div>
    </div>

    <div class="divider"></div>

    <div class="address">
      <div>4820 Bramblewood Lane,</div>
      <div>Suite 317 Estero, FL 33961</div>
    </div>
  </section>

  <section class="card card-back">
    <div class="back-circle"></div>
  </section>
</body>
</html>
```